Flyer design for our aerial photography service

We need an 8.5x11 two sided design flyer that will showcase our aerial photography service. No pricing or text is needed aside from our logo and somewhere on the page the title "Aerial Photography". I would like it be a black background with our logo in white which I have attached. Please make it a creative stylish design that highlights the photos. Our Logo should be at the top. The logo should not be large and shouldnt be the focus of the page but should be fairly visible. I'm open to it being in different locations as well.

Industry/Entity Type

Real Estate

Font styles to use
Serif

Requirements
Must have
• Logo and photos and the title Aerial Photography
Nice to have
Should not have
• n/a

```html
<!DOCTYPE html>
<html lang="en">
<head>
<meta charset="utf-8">
<title>Aerial Photography Flyer</title>
<link href="https://fonts.googleapis.com/css2?family=Cinzel:wght@400;500&family=Lato:wght@400&family=Roboto+Condensed:wght@400;700&display=swap" rel="stylesheet">
<style>
  :root {
    --green: #4dbb56;
    --green-text: #5ccf4f;
    --black: #050505;
    --gold-light: #e9c46a;
    --gold: #b8872e;
    --gold-dark: #6f4a12;
    --white: #ffffff;
    --ink: #111111;
  }
  html, body { margin: 0; padding: 0; overflow: hidden; }
  body { width: 900px; height: 1200px; background: var(--black); }
  .flyer { position: relative; width: 900px; height: 1200px; overflow: hidden; background: var(--black); font-family: "Lato", sans-serif; color: var(--white); }
  .side-band { position: absolute; left: 0; top: 0; width: 420px; height: 1200px; background: var(--green); }
  .frame { position: absolute; box-sizing: border-box; padding: 6px; background: linear-gradient(135deg, var(--gold-light), var(--gold) 45%, var(--gold-dark) 70%, var(--gold-light)); }
  .frame .photo { width: 100%; height: 100%; }
  .hero { left: 30px; top: 20px; width: 840px; height: 410px; }
  .hero .photo { background: radial-gradient(ellipse at 50% 45%, #6b7480 0%, #3c4a3a 30%, #1f3a1c 60%, #142712 100%); }
  .thumb-1 { left: 24px; top: 452px; width: 392px; height: 226px; }
  .thumb-1 .photo { background: linear-gradient(160deg, #4f6a55 0%, #8c8a7a 35%, #6b5a48 55%, #3a6a3c 80%, #254d2a 100%); }
  .thumb-2 { left: 24px; top: 688px; width: 392px; height: 230px; }
  .thumb-2 .photo { background: linear-gradient(180deg, #23401f 0%, #35582f 45%, #9a9588 62%, #2f4a3e 78%, #1d3833 100%); }
  .thumb-3 { left: 24px; top: 928px; width: 392px; height: 230px; }
  .thumb-3 .photo { background: linear-gradient(175deg, #b8c6d2 0%, #4f6c4a 18%, #6e8b9a 32%, #7b7670 55%, #4f4a44 80%, #3f5a35 100%); }
  .title-plate { position: absolute; left: 420px; top: 440px; width: 450px; height: 150px; }
  .title-plate svg { position: absolute; inset: 0; }
  .brand { position: absolute; left: 0; right: 0; top: 30px; text-align: center; }
  .brand-mark { display: block; width: 30px; height: 30px; margin: 0 auto 8px; border: 2px solid var(--white); border-radius: 50%; box-sizing: border-box; }
  .brand-name { font-family: "Cinzel", serif; font-weight: 400; font-size: 14px; letter-spacing: 0.5px; color: var(--white); margin: 0; }
  .service-title { position: absolute; left: 0; right: 0; top: 98px; margin: 0; text-align: center; font-family: "Cinzel", serif; font-weight: 400; font-size: 27px; letter-spacing: 1px; color: var(--white); }
  .info { position: absolute; left: 443px; width: 412px; }
  .info h2 { margin: 0 0 20px; font-family: "Roboto Condensed", sans-serif; font-weight: 700; font-size: 19px; color: var(--green-text); display: inline-block; padding-bottom: 6px; border-bottom: 1px solid var(--green-text); }
  .info p { margin: 0 0 18px; font-size: 13.5px; line-height: 1.36; text-align: justify; }
  .about { top: 622px; }
  .aerial { top: 800px; }
  .contact { position: absolute; left: 420px; top: 1030px; width: 480px; height: 170px; color: var(--ink); }
  .contact svg.plate { position: absolute; inset: 0; }
  .contact-body { position: absolute; left: 90px; top: 30px; font-family: "Roboto Condensed", sans-serif; }
  .row { display: flex; align-items: center; gap: 6px; }
  .address { font-size: 13px; line-height: 1.2; font-weight: 700; padding-bottom: 6px; border-bottom: 1px solid var(--ink); width: 240px; }
  .phone { margin-top: 10px; font-size: 28px; font-weight: 700; letter-spacing: 0.5px; }
  .email { margin-top: 2px; font-size: 13px; font-weight: 700; }
  .icon { flex: none; }
</style>
</head>
<body>
<main class="flyer">
  <div class="side-band"></div>

  <div class="frame hero"><div class="photo" role="img" aria-label="Aerial view at dusk of a large two-storey house with dark roof, lit windows and surrounding trees"></div></div>
  <div class="frame thumb-1"><div class="photo" role="img" aria-label="Aerial view of a hillside home with pool and multi-level wooden deck"></div></div>
  <div class="frame thumb-2"><div class="photo" role="img" aria-label="Aerial view of a lakeside house with dock and boat among trees"></div></div>
  <div class="frame thumb-3"><div class="photo" role="img" aria-label="Aerial view of a lake house with garage and driveway, lake and hills behind"></div></div>

  <header class="title-plate">
    <svg width="450" height="150" viewBox="0 0 450 150">
      <defs>
        <linearGradient id="goldEdge" x1="0" y1="0" x2="1" y2="0">
          <stop offset="0" stop-color="#6f4a12"/><stop offset="0.35" stop-color="#e9c46a"/><stop offset="0.7" stop-color="#b8872e"/><stop offset="1" stop-color="#e9c46a"/>
        </linearGradient>
      </defs>
      <polygon points="0,0 450,0 430,82 398,142 52,142 20,82" fill="url(#goldEdge)"/>
      <polygon points="8,5 442,5 424,80 393,136 57,136 26,80" fill="#050505"/>
      <polyline points="34,82 60,128 390,128 416,82" fill="none" stroke="url(#goldEdge)" stroke-width="2"/>
      <line x1="150" y1="84" x2="300" y2="84" stroke="#5ccf4f" stroke-width="1"/>
    </svg>
    <div class="brand">
      <span class="brand-mark"></span>
      <p class="brand-name">Skyline Frame Studio</p>
    </div>
    <h1 class="service-title">AERIAL PHOTOGRAPHY</h1>
  </header>

  <section class="info about">
    <h2>About Us</h2>
    <p>Skyline Frame Studio is a team of enthusiastic, creative professionals dedicated to providing our Real Estate clients with the finest and most up-to-date marketing tools available. Consistent exceptional quality, fast delivery, competitive pricing and ease of booking are our promises.</p>
  </section>

  <section class="info aerial">
    <h2>Aerial Photography</h2>
    <p>Aerial Photography is the best way to showcase your listings property.</p>
    <p>Capturing a property from above can provide a dramatic look into the size of lot. These aerial images are sure to stop people in their tracks when they come across your listing on the MLS.</p>
  </section>

  <footer class="contact">
    <svg class="plate" width="480" height="170" viewBox="0 0 480 170">
      <defs>
        <linearGradient id="goldPlate" x1="0" y1="0" x2="1" y2="1">
          <stop offset="0" stop-color="#e6c06a"/><stop offset="0.45" stop-color="#b8862e"/><stop offset="0.75" stop-color="#d9ad55"/><stop offset="1" stop-color="#7a5216"/>
        </linearGradient>
      </defs>
      <polygon points="30,0 430,0 480,60 480,170 0,170 0,110" fill="url(#goldPlate)"/>
    </svg>
    <div class="contact-body">
      <div class="row address">
        <svg class="icon" width="18" height="16" viewBox="0 0 18 16"><path d="M9 1 L1 8 H3.5 V15 H7.5 V10.5 H10.5 V15 H14.5 V8 H17 Z" fill="#111"/></svg>
        <span>Skyline Frame Studio, LLC<br>18 Willow Bend Rd, Cedar Grove, NJ 07009</span>
      </div>
      <div class="row phone">
        <svg class="icon" width="20" height="22" viewBox="0 0 20 22"><circle cx="10" cy="11" r="9" fill="none" stroke="#111" stroke-width="1.6"/><path d="M7 6 C5.5 9 7 14 11 16 L12.5 14.5 L10.8 12.8 L9.8 13.5 C8.6 12.5 8 11 8 9.5 L9 8.8 L8.2 6.5 Z" fill="#111"/></svg>
        <span>1 555 014 2280</span>
      </div>
      <div class="row email">
        <svg class="icon" width="14" height="10" viewBox="0 0 14 10"><rect x="0.5" y="0.5" width="13" height="9" fill="#111"/><polyline points="0.5,0.5 7,5.5 13.5,0.5" fill="none" stroke="#c9a04a" stroke-width="1"/></svg>
        <span>hello@skylineframestudio.com</span>
      </div>
    </div>
  </footer>
</main>
</body>
</html>
```